Basic Web Redesign

Hello,

We are working with a client who would like their existing website updated.

The site is http://www.lorenvasquel.com/

Currently the website is Joomla 1.0.x with Virtuemart running the small online shop.

We are extremely flexible with regards to the way forward - i.e. it can be Joomla 2.5 with Virtuemart, Wordpress plus a shopping cart, HTML 5 (no CMS) with a shopping cart or a full blown ecommerce solution using Prestashop, Magento etc.

The main constraint is a website that incorporates a working shop. At this moment the current website works, but is on extremely old versions of Joomla and Virtuemart.

So the brief is to either migrate the existing offering to a newer version of Joomla and Virtuemart OR use alternative products to achieve a very basic website with shopping cart functionality.

Reason: To enable designer to upload files and installation to be tested.

Target Market(s)

Predominantly people living on the Costa Blanca in Spain, but also some customers in the UK.

Industry/Entity Type

Shop

Requirements
Must have
• Online shop
Shipping calculator
PayPal for accepting payments
Nice to have
• Easy to use front-end for editing shop items
Easy to use front-end for editing non-shop pages

```html
<!DOCTYPE html>
<html lang="en">
<head>
<meta charset="utf-8">
<title>Flower Shop</title>
<link rel="stylesheet" href="https://fonts.googleapis.com/css2?family=Arimo:wght@400;700&display=swap">
<style>
:root{
  --red:#a8191c;
  --red-dark:#8c1214;
  --title:#9b1b1e;
  --text:#222;
  --muted:#777;
  --line:#cfcfcf;
  --card-border:#dcdcdc;
  --header-wood:#4a4540;
  --orange:#f39200;
  --green-badge:#b5d335;
  --promo-badge:#e8471c;
}
*{box-sizing:border-box;margin:0;padding:0}
html,body{width:927px;height:1200px;overflow:hidden;background:#fff}
body{position:relative;font-family:"Arimo",Arial,sans-serif;color:var(--text)}
.abs{position:absolute}

/* header */
.site-header{left:0;top:0;width:927px;height:187px;
  background:linear-gradient(90deg,#3b3733 0%,#5b544c 35%,#6a625a 55%,#4e4843 80%,#3a3633 100%)}
.header-art{left:520px;top:0;width:407px;height:130px;
  background:radial-gradient(ellipse at 60% 40%,rgba(200,60,80,.55),rgba(90,70,60,0) 70%)}
.brand{left:32px;top:0;width:195px;height:67px;background:var(--red);
  border-bottom:2px dashed rgba(255,255,255,.35);display:flex;align-items:center;padding-left:16px;gap:12px}
.brand-mark{width:14px;height:14px;background:#fff}
.brand-name{color:#fff;font-size:22px;font-weight:400}
.main-nav{left:29px;top:127px;width:642px;height:40px;background:rgba(255,255,255,.12);
  display:flex;align-items:center;padding-left:12px;gap:0}
.main-nav a{color:#fff;text-decoration:none;font-size:13.5px;padding:5px 11px;margin-right:6px}
.main-nav a.active{background:var(--red)}

/* columns */
.left-col{left:0;top:187px;width:527px;height:884px;
  background:linear-gradient(90deg,#fff 0%,#fff 68%,#ececec 100%)}
.section-title{font-size:19.5px;color:var(--title);display:flex;align-items:center;gap:8px;font-weight:400}
.flower-icon{width:22px;height:22px}
.photo{border-radius:2px}
.product-box{width:301px;height:143px;border:1px solid var(--card-border);border-radius:6px;background:#fff;padding:14px 14px}
.product-box h3{font-size:13.5px;font-weight:400;color:var(--title);margin-bottom:6px}
.product-box p{font-size:11px;line-height:18px;text-align:justify}
.more{position:absolute;right:14px;bottom:10px;font-size:10.5px;color:var(--title);font-style:normal}
.dash{border-top:1px dashed #bbb;height:0}
.tile-name{font-size:12px;color:var(--muted);text-align:center;width:136px}
.tile{width:136px;height:122px;border:1px solid var(--card-border);border-radius:6px;background:#fff;overflow:hidden}
.tile .photo{position:absolute;left:30px;top:14px;width:76px;height:94px}
.ribbon{position:absolute;right:0;top:0}

/* sidebar */
.lang{left:547px;top:206px;font-size:12px;display:flex;align-items:center;gap:5px}
.flag{width:16px;height:11px;border:1px solid #aaa}
.currency{left:708px;top:203px;font-size:12px;display:flex;align-items:center;gap:4px}
.cur{border:1px solid #ddd;padding:3px 4px}
.cur.on{background:var(--orange);color:#fff;border-color:var(--orange);font-weight:700}
.cart{left:547px;top:248px;display:flex;align-items:center;gap:6px;font-size:19px;color:var(--title)}
.cart-summary{left:652px;top:251px;border:1px solid #ddd;font-size:11px;padding:3px 5px}
.cart-link{left:802px;top:251px;font-size:11.5px;color:var(--title);text-decoration:underline}
.hatch{left:547px;width:344px;height:10px;
  background:repeating-linear-gradient(45deg,#e2e2e2 0 2px,#fff 2px 4px)}
.about-text{left:547px;top:361px;width:206px;font-size:12.5px;line-height:20px;text-align:justify}
.side-list{list-style:none;font-size:12.5px;line-height:19.6px}
.side-list li::before{content:"»";color:#999;margin-right:8px}
.promo-name{font-size:12px;color:var(--muted);width:136px;text-align:center}

/* footer */
.footer-rule{left:0;top:1071px;width:927px;border-top:1px dashed #ccc}
.footer-brand{left:13px;top:1086px;font-size:19px;color:#999}
.footer-nav{right:15px;top:1083px;font-size:12.5px;display:flex;gap:16px}
.footer-nav a{color:#999;text-decoration:none}
.footer-art{left:0;top:1116px;width:927px;height:57px;
  background:linear-gradient(90deg,rgba(80,160,200,.35),rgba(240,200,60,.35),rgba(200,70,120,.35),rgba(120,180,90,.35),rgba(230,80,80,.35))}
.footer-band{left:0;top:1173px;width:927px;height:27px;background:#c8c8c8}
</style>
</head>
<body>

<header class="site-header abs">
  <div class="header-art abs" role="img" aria-label="Wooden fence with climbing branches and colourful painted flowers"></div>
  <div class="brand abs"><span class="brand-mark"></span><span class="brand-name">flower shop</span></div>
  <nav class="main-nav abs">
    <a class="active" href="#">home</a><a href="#">about us</a><a href="#">flowers</a><a href="#">specials gifts</a><a href="#">my accout</a><a href="#">register</a><a href="#">prices</a><a href="#">contact</a>
  </nav>
</header>

<main>
  <div class="left-col abs"></div>

  <h2 class="section-title abs" style="left:22px;top:216px">
    <svg class="flower-icon" viewBox="0 0 22 22"><g fill="#c0282b"><circle cx="11" cy="5" r="5"/><circle cx="17" cy="11" r="5"/><circle cx="11" cy="17" r="5"/><circle cx="5" cy="11" r="5"/></g><circle cx="11" cy="11" r="2.5" fill="#fff"/></svg>
    Featured products</h2>

  <div class="photo abs" style="left:20px;top:267px;width:153px;height:140px;background:radial-gradient(ellipse at 50% 40%,#f2d23a,#c9a826 45%,#5f8a5a 75%,#fff 76%)" role="img" aria-label="Yellow lily bouquet in a teal vase"></div>
  <article class="product-box abs" style="left:196px;top:264px">
    <h3>Product name</h3>
    <p>Lorem ipsum dolor sit amet, consectetur adipisicing elit, sed do eiusmod tempor incididunt ut labore et dolore magna aliqua. Ut enim ad minim veniam, quis nostrud exercitation.</p>
    <span class="more">- more details -</span>
  </article>
  <div class="dash abs" style="left:20px;top:417px;width:484px"></div>

  <div class="photo abs" style="left:28px;top:455px;width:135px;height:138px;background:radial-gradient(ellipse at 50% 40%,#c88aa8,#8a4a78 45%,#7a9a6a 72%,#fff 73%)" role="img" aria-label="Pink and purple mixed bouquet in a glass vase"></div>
  <article class="product-box abs" style="left:196px;top:450px">
    <h3>Product name</h3>
    <p>Lorem ipsum dolor sit amet, consectetur adipisicing elit, sed do eiusmod tempor incididunt ut labore et dolore magna aliqua. Ut enim ad minim veniam, quis nostrud exercitation.</p>
    <span class="more">- more details -</span>
  </article>
  <div class="dash abs" style="left:20px;top:604px;width:484px"></div>

  <h2 class="section-title abs" style="left:22px;top:635px">
    <svg class="flower-icon" viewBox="0 0 22 22"><g fill="#3a8fd6"><circle cx="11" cy="5" r="5"/><circle cx="17" cy="11" r="5"/><circle cx="11" cy="17" r="5"/><circle cx="5" cy="11" r="5"/></g><circle cx="11" cy="11" r="3" fill="#f2c12e"/></svg>
    New products</h2>

  <div class="tile-name abs" style="left:31px;top:687px">product name</div>
  <div class="tile abs" style="left:31px;top:707px">
    <div class="photo" role="img" aria-label="Pink tulips in a glass vase" style="background:radial-gradient(ellipse at 50% 35%,#f09ab8,#6fa86a 60%,#fff 61%)"></div>
    <svg class="ribbon" width="50" height="50" viewBox="0 0 50 50"><path d="M12 0h16l22 22v16z" fill="var(--green-badge)"/><text x="36" y="18" transform="rotate(45 36 18)" font-size="9" fill="#fff" text-anchor="middle" font-family="Arimo,sans-serif">NEW</text></svg>
  </div>
  <div class="tile-name abs" style="left:188px;top:687px">product name</div>
  <div class="tile abs" style="left:188px;top:707px">
    <div class="photo" role="img" aria-label="Pink and purple mixed bouquet" style="background:radial-gradient(ellipse at 50% 35%,#c88aa8,#7a9a6a 60%,#fff 61%)"></div>
    <svg class="ribbon" width="50" height="50" viewBox="0 0 50 50"><path d="M12 0h16l22 22v16z" fill="var(--green-badge)"/><text x="36" y="18" transform="rotate(45 36 18)" font-size="9" fill="#fff" text-anchor="middle" font-family="Arimo,sans-serif">NEW</text></svg>
  </div>
  <div class="tile-name abs" style="left:344px;top:687px">product name</div>
  <div class="tile abs" style="left:344px;top:707px">
    <div class="photo" role="img" aria-label="Yellow lily bouquet in a teal vase" style="background:radial-gradient(ellipse at 50% 35%,#f2d23a,#4f8a80 62%,#fff 63%)"></div>
    <svg class="ribbon" width="50" height="50" viewBox="0 0 50 50"><path d="M12 0h16l22 22v16z" fill="var(--green-badge)"/><text x="36" y="18" transform="rotate(45 36 18)" font-size="9" fill="#fff" text-anchor="middle" font-family="Arimo,sans-serif">NEW</text></svg>
  </div>
</main>

<aside>
  <div class="lang abs">Languages:
    <span class="flag" style="background:linear-gradient(#c8102e,#c8102e) center/100% 3px no-repeat,linear-gradient(#c8102e,#c8102e) center/3px 100% no-repeat,#1d3f8a"></span>
    <span class="flag" style="background:linear-gradient(90deg,#2a4aa0 33%,#fff 33% 66%,#d52b1e 66%)"></span>
    <span class="flag" style="background:linear-gradient(#000 33%,#d00 33% 66%,#f5c400 66%)"></span>
  </div>
  <div class="currency abs">Currency: <span class="cur">GBP</span><span class="cur">EUR</span><span class="cur on">USD</span></div>

  <div class="cart abs">
    <svg width="22" height="20" viewBox="0 0 22 20"><path d="M1 2h4l3 11h10l3-8H7" fill="none" stroke="var(--orange)" stroke-width="2"/><circle cx="9" cy="17" r="2" fill="var(--orange)"/><circle cx="17" cy="17" r="2" fill="var(--orange)"/></svg>
    My cart</div>
  <div class="cart-summary abs">3 x items | TOTAL: 100$</div>
  <a class="cart-link abs" href="#">view cart</a>
  <div class="hatch abs" style="top:287px"></div>

  <h2 class="section-title abs" style="left:549px;top:320px">
    <svg class="flower-icon" viewBox="0 0 22 22"><circle cx="11" cy="11" r="10" fill="#3c9a3c"/><circle cx="11" cy="11" r="4" fill="#f2c12e"/></svg>
    About Our Shop</h2>
  <p class="about-text abs">Lorem ipsum dolor sit amet, consectetur adipisicing elit, sed do eiusmod tempor incididunt ut labore et dolore magna aliqua. Ut enim ad minim veniam, quis nostrud</p>
  <div class="photo abs" style="left:763px;top:361px;width:130px;height:88px;background:linear-gradient(135deg,#6a8a4a,#a8c070 45%,#8a6a5a)" role="img" aria-label="Flower shop storefront with potted plants"></div>
  <div class="hatch abs" style="top:473px"></div>

  <h2 class="section-title abs" style="left:549px;top:506px">
    <svg class="flower-icon" viewBox="0 0 22 22"><path d="M11 1l3 7 7 3-7 3-3 7-3-7-7-3 7-3z" fill="#d94a4a"/><circle cx="11" cy="11" r="2.5" fill="#3a8fd6"/></svg>
    Promotions</h2>
  <h2 class="section-title abs" style="left:724px;top:506px">
    <svg class="flower-icon" viewBox="0 0 22 22"><path d="M11 1l3 7 7 3-7 3-3 7-3-7-7-3 7-3z" fill="none" stroke="#c8702a" stroke-width="1.6"/></svg>
    Categories</h2>

  <div class="promo-name abs" style="left:557px;top:559px">product name</div>
  <div class="tile abs" style="left:557px;top:577px">
    <div class="photo" role="img" aria-label="Pink tulips in a glass vase" style="background:radial-gradient(ellipse at 50% 35%,#f09ab8,#6fa86a 60%,#fff 61%)"></div>
    <svg class="ribbon" width="50" height="50" viewBox="0 0 50 50"><path d="M12 0h16l22 22v16z" fill="var(--promo-badge)"/><text x="36" y="18" transform="rotate(45 36 18)" font-size="9" fill="#fff" text-anchor="middle" font-family="Arimo,sans-serif">-10%</text></svg>
  </div>
  <div class="promo-name abs" style="left:557px;top:729px">product name</div>
  <div class="tile abs" style="left:557px;top:747px">
    <div class="photo" role="img" aria-label="Pink and purple mixed bouquet" style="background:radial-gradient(ellipse at 50% 35%,#c88aa8,#7a9a6a 60%,#fff 61%)"></div>
    <svg class="ribbon" width="50" height="50" viewBox="0 0 50 50"><path d="M12 0h16l22 22v16z" fill="var(--promo-badge)"/><text x="36" y="18" transform="rotate(45 36 18)" font-size="9" fill="#fff" text-anchor="middle" font-family="Arimo,sans-serif">-10%</text></svg>
  </div>
  <div class="promo-name abs" style="left:557px;top:898px">product name</div>
  <div class="tile abs" style="left:557px;top:916px">
    <div class="photo" role="img" aria-label="Yellow lily bouquet in a teal vase" style="background:radial-gradient(ellipse at 50% 35%,#f2d23a,#4f8a80 62%,#fff 63%)"></div>
    <svg class="ribbon" width="50" height="50" viewBox="0 0 50 50"><path d="M12 0h16l22 22v16z" fill="var(--promo-badge)"/><text x="36" y="18" transform="rotate(45 36 18)" font-size="9" fill="#fff" text-anchor="middle" font-family="Arimo,sans-serif">-10%</text></svg>
  </div>

  <ul class="side-list abs" style="left:742px;top:552px">
    <li>accesories</li><li>flower gifts</li><li>specials</li><li>hollidays gifts</li><li>accesories</li><li>flower gifts</li><li>specials</li><li>hollidays gifts</li><li>accesories</li><li>flower gifts</li><li>specials</li>
  </ul>

  <h2 class="section-title abs" style="left:724px;top:779px">
    <svg class="flower-icon" viewBox="0 0 22 22"><g fill="#8cc63f"><circle cx="11" cy="5" r="5"/><circle cx="17" cy="11" r="5"/><circle cx="11" cy="17" r="5"/><circle cx="5" cy="11" r="5"/></g><circle cx="11" cy="11" r="3" fill="#f2c12e"/></svg>
    Partners</h2>
  <ul class="side-list abs" style="left:742px;top:825px">
    <li>accesories</li><li>flower gifts</li><li>specials</li><li>hollidays gifts</li><li>accesories</li><li>flower gifts</li><li>specials</li><li>hollidays gifts</li><li>accesories</li>
  </ul>
</aside>

<footer>
  <div class="footer-rule abs"></div>
  <div class="footer-brand abs">flower shop</div>
  <nav class="footer-nav abs"><a href="#">home</a><a href="#">about us</a><a href="#">services</a><a href="#">privacy policy</a><a href="#">contact us</a></nav>
  <div class="footer-art abs" role="img" aria-label="Row of colourful illustrated flowers"></div>
  <div class="footer-band abs"></div>
</footer>

</body>
</html>
```